Cover für Erstlingswerk
Ich habe von Ralosa ein phantastisches Cover für mein Buch bekommen. Ganz anders als ich es mir bei Auftragsstellung vorgestellt habe. Sehr innovativ und außergewöhnlich. Die Zusammenarbeit war freundlich und locker, spontan und flexibel. Ich bedanke mich ganz herzlich für dieses wundervolle Cover für mein Herzensprojekt!
Zielgruppe
Es handelt sich um einen Roman, der insbesondere Frauen zwischen 30 und 60 Jahren ansprechen wird.
Aufgabenstellung
Das Cover soll schlicht, ohne Schnörkel sein, bevorzugte Farben blau wie die Nordsee und der Himmel, grün und braun wie der Kiefernwald und das Dünengras und weiß wie die Wolken. Ggf. ein Bezug zu Dänemark. Aber ich bin für alle Ideen offen.
Noch ein Nachtrag: dies ist mein erster Auftrag und mein erstes Buch, daher, wenn es Fragen gibt, bitte stellen. Ich habe auch einen Klappentext, wird der zu diesem Zeitpunkt schon eingebunden? Es steckt viel Herzblut und Zeit in meinem ersten Roman. Wenn ich für das Cover mehr Input geben soll, bitte mitteilen!
Noch ein Nachtrag: Der Titel des Buches lautet "Wo der Wind mich fand" und der Name der Autorin Marla Thorvik.

```html
<!DOCTYPE html>
<html lang="de">
<head>
<meta charset="utf-8">
<title>Wo der Wind mich fand – Buchcover</title>
<link rel="stylesheet" href="https://fonts.googleapis.com/css2?family=Dancing+Script:wght@500&family=Overlock:wght@400&display=swap">
<style>
  :root {
    --page-bg: #e9e9e8;
    --sky-light: #c9d3d8;
    --sky-mid: #aebcc4;
    --sky-deep: #8fa3ae;
    --portrait-dark: #2c4458;
    --portrait-mid: #4f6f82;
    --sea-teal: #5f8c86;
    --dune-brown: #4d4e3c;
    --author-ink: #4a6673;
    --title-white: #ffffff;
  }
  * { margin: 0; padding: 0; box-sizing: border-box; }
  html, body {
    width: 1200px;
    height: 800px;
    overflow: hidden;
    background: var(--page-bg);
  }
  .canvas {
    position: relative;
    width: 1200px;
    height: 800px;
    display: flex;
    align-items: center;
    justify-content: center;
  }
  .cover {
    position: relative;
    width: 484px;
    height: 744px;
    overflow: hidden;
    background: linear-gradient(180deg, var(--sky-mid) 0%, var(--sky-light) 45%, var(--sky-mid) 100%);
  }
  .cover-sky {
    position: absolute;
    inset: 0;
    background:
      radial-gradient(ellipse at 50% 35%, rgba(255,255,255,0.35), transparent 60%),
      linear-gradient(180deg, var(--sky-deep) 0%, var(--sky-light) 40%, var(--sky-mid) 100%);
  }
  .cover-portrait {
    position: absolute;
    left: 20%;
    top: 33%;
    width: 60%;
    height: 67%;
    border-radius: 46% 46% 0 0 / 28% 28% 0 0;
    background: linear-gradient(180deg,
      var(--portrait-dark) 0%,
      var(--portrait-mid) 40%,
      var(--sky-mid) 58%,
      var(--sea-teal) 75%,
      var(--dune-brown) 100%);
    opacity: 0.9;
  }
  .author {
    position: absolute;
    top: 70px;
    width: 100%;
    text-align: center;
    font-family: "Overlock", sans-serif;
    font-size: 38px;
    letter-spacing: 0.5px;
    color: var(--author-ink);
  }
  .title {
    position: absolute;
    left: 78px;
    top: 290px;
    font-family: "Dancing Script", cursive;
    font-weight: 500;
    color: var(--title-white);
    line-height: 0.95;
  }
  .title-line { display: block; font-size: 80px; }
  .title-line--second { padding-left: 28px; }
  .title-line--last { font-size: 118px; padding-left: 34px; }
  .genre {
    position: absolute;
    right: 40px;
    top: 568px;
    font-family: "Overlock", sans-serif;
    font-size: 25px;
    color: var(--author-ink);
  }
</style>
</head>
<body>
  <main class="canvas">
    <section class="cover" aria-label="Buchcover">
      <div class="cover-sky" role="img" aria-label="Wolkenhimmel über der Nordsee als Hintergrund"></div>
      <div class="cover-portrait" role="img" aria-label="Doppelbelichtung: Profil einer Frau, gefüllt mit Wolken, Meer und Strand"></div>
      <p class="author">Marla Thorvik</p>
      <h1 class="title">
        <span class="title-line">Wo der</span>
        <span class="title-line title-line--second">Wind mich</span>
        <span class="title-line title-line--last">fand</span>
      </h1>
      <p class="genre">Roman</p>
    </section>
  </main>
</body>
</html>
```